Plain Larder 100% real ingredients

I need a label design for my hummus.
"Big Whoa" Hummus
Roasted Red Pepper hummus infused with Crushed Red Pepper for a kick
Made With Real Ingredients
Oil Free
Preservative Free
in small print: PlainLarderNaturalFoods.example
I also need an ingredient list
Chickpeas, Tahini, Red bell pepper, Sweet onion, Garlic, Water, Lemon, Maple syrup, Crushed red pepper, Pink Himalayan salt, Cumin, Cayenne, Black pepper,Baking soda
In our Hummus:
We believe that our hummus doesn't need all the extra ingredients like oils and preservatives. We want you to feel good after eating our products while also eating good food that is good for you! So we use fresh ingredients like lemon, garlic, red peppers, and sweet onions.
In the design can you put a red roasted pepper in the background?
Two of the pictures I uploaded are examples of what I would like it to look like.

```html
<!DOCTYPE html>
<html lang="en">
<head>
<meta charset="utf-8">
<title>"Big Whoa" Hummus Label</title>
<link rel="stylesheet" href="https://fonts.googleapis.com/css2?family=Cinzel+Decorative:wght@700&family=Marcellus&family=Cormorant+Garamond:wght@500&display=swap">
<style>
  :root {
    --paper: #ffffff;
    --ink: #1d1a1a;
    --stage: #c1c1c1;
    --stage-edge: #8a8a8a;
    --pepper-light: #c8342a;
    --pepper-dark: #5e1512;
  }
  html, body {
    margin: 0;
    padding: 0;
    width: 1200px;
    height: 757px;
    overflow: hidden;
    background: var(--paper);
  }
  .canvas { display: block; width: 1200px; height: 757px; }
  .stage { fill: var(--stage); stroke: var(--stage-edge); stroke-width: 0.6; }
  .guide { stroke: var(--stage-edge); stroke-width: 0.6; }
  .label-body { fill: var(--paper); filter: url(#label-shadow); }
  .frame-heavy { fill: none; stroke: var(--ink); stroke-width: 3.5; }
  .frame-fine { fill: none; stroke: var(--ink); stroke-width: 1; }
  .band { fill: var(--ink); }
  .medallion { fill: var(--paper); }
  .brand-name { font-family: "Marcellus", serif; font-size: 20px; fill: var(--ink); letter-spacing: 0.5px; }
  .brand-percent { font-family: "Marcellus", serif; font-size: 27px; fill: var(--ink); }
  .arch-claim { font-family: "Cormorant Garamond", serif; font-weight: 500; font-size: 11px; fill: var(--ink); letter-spacing: 7px; }
  .claim { font-family: "Cormorant Garamond", serif; font-weight: 500; font-size: 15px; fill: var(--ink); }
  .section-head { font-family: "Marcellus", serif; font-size: 14px; fill: var(--ink); letter-spacing: 0.3px; }
  .ingredients { font-family: "Cormorant Garamond", serif; font-weight: 500; font-size: 10.5px; fill: var(--paper); }
  .badge-ring { fill: none; stroke: var(--paper); }
  .badge-text { font-family: "Cormorant Garamond", serif; font-weight: 500; font-size: 10.5px; fill: var(--paper); letter-spacing: 0.6px; }
  .product-name { font-family: "Cinzel Decorative", serif; font-weight: 700; font-size: 56px; fill: var(--ink); }
  .rule { stroke: var(--ink); stroke-width: 1.6; }
  .tagline { font-family: "Marcellus", serif; font-size: 12.6px; fill: var(--ink); }
  .web-pill { fill: var(--ink); }
  .web-address { font-family: "Cormorant Garamond", serif; font-weight: 500; font-size: 12.5px; fill: var(--paper); }
</style>
</head>
<body>
<svg class="canvas" viewBox="0 0 1200 757" xmlns="http://www.w3.org/2000/svg">
  <defs>
    <filter id="label-shadow" x="-20%" y="-20%" width="140%" height="150%">
      <feDropShadow dx="0" dy="10" stdDeviation="14" flood-color="#000" flood-opacity="0.35"/>
    </filter>
    <linearGradient id="pepper-tone" x1="0" y1="0" x2="0" y2="1">
      <stop offset="0" stop-color="var(--pepper-light)"/>
      <stop offset="1" stop-color="var(--pepper-dark)"/>
    </linearGradient>
    <path id="arch-path" d="M533.7,139.6 A88,88 0 0 1 596.3,302.7"/>
    <path id="badge-path" d="M306.7,373.3 A40,40 0 1 1 363.3,373.3"/>
  </defs>

  <rect class="stage" x="0" y="0" width="1133" height="670"/>
  <line class="guide" x1="897" y1="198" x2="897" y2="596"/>

  <g class="label">
    <g class="label-body">
      <rect x="249" y="210" width="614" height="327" rx="20"/>
      <circle cx="555" cy="221" r="119"/>
      <rect x="461" y="515" width="189" height="34" rx="16"/>
    </g>

    <rect class="band" x="277" y="287" width="553" height="114"/>
    <circle class="medallion" cx="555" cy="221" r="112"/>

    <path class="frame-heavy" d="M444,217 H266 A10,10 0 0 0 256,227 V520 A10,10 0 0 0 266,530 H847 A10,10 0 0 0 857,520 V227 A10,10 0 0 0 847,217 H666 A111,111 0 1 0 444,217 Z"/>
    <path class="frame-fine" d="M449,222 H268 A6,6 0 0 0 262,228 V519 A6,6 0 0 0 268,525 H845 A6,6 0 0 0 851,519 V228 A6,6 0 0 0 845,222 H661 A106,106 0 1 0 449,222"/>

    <text class="arch-claim"><textPath href="#arch-path">REAL INGREDIENTS</textPath></text>
    <text class="brand-name" x="560" y="214" text-anchor="middle">PLAIN LARDER</text>
    <text class="brand-percent" x="558" y="254" text-anchor="middle">100%</text>

    <text class="claim" x="279" y="278">Oil &amp; Preservative Free</text>
    <text class="section-head" x="825" y="280" text-anchor="end">INGREDIENTS</text>

    <g class="badge">
      <circle class="badge-ring" cx="335" cy="345" r="49" stroke-width="2"/>
      <circle class="badge-ring" cx="335" cy="345" r="32" stroke-width="1.5"/>
      <text class="badge-text"><textPath href="#badge-path">MADE WITH REAL INGREDIENTS</textPath></text>
    </g>

    <text class="ingredients" text-anchor="end">
      <tspan x="825" y="315">Chickpeas, Tahini, Red bell pepper,</tspan>
      <tspan x="825" y="332">Sweet onion, Garlic, Water, Lemon,</tspan>
      <tspan x="825" y="349">Maple syrup, Crushed red pepper,</tspan>
      <tspan x="825" y="365">Pink Himalayan salt, Cumin,</tspan>
      <tspan x="825" y="382">Cayenne, Black pepper, Baking soda.</tspan>
    </text>

    <rect class="pepper-art" x="462" y="300" width="198" height="110" rx="22" fill="url(#pepper-tone)" role="img" aria-label="Illustration of two roasted red bell peppers"/>

    <text class="product-name" x="558" y="463" text-anchor="middle" textLength="545" lengthAdjust="spacingAndGlyphs">“BIG WHOA” HUMMUS</text>

    <line class="rule" x1="285" y1="480" x2="833" y2="480"/>
    <text class="tagline" x="559" y="497" text-anchor="middle" textLength="540" lengthAdjust="spacingAndGlyphs">ROASTED RED PEPPER HUMMUS INFUSED WITH CRUSHED RED PEPPER FOR A KICK</text>
    <line class="rule" x1="285" y1="503" x2="833" y2="503"/>

    <rect class="web-pill" x="466" y="520" width="180" height="23" rx="11.5"/>
    <text class="web-address" x="556" y="536" text-anchor="middle">PlainLarderNaturalFoods.example</text>
  </g>
</svg>
</body>
</html>
```